IT supplier clean wordpress website - payment guaranteed

Clean website design for a wordpress based website
Design only - PSD delivery with images

current website: www.quorvel.net
please use your imagination and try something out of the box...
We like https://tavrinex.com.au as look and feel, but you don't have to copy it, you can be creative

We like the navigation header and the phone number, but do not need 'instant quote' so the 1300 phone number and the 'lock' icon for login can be on the same line

Site Map:
IT support
VoIP
Internet and Data
Cloud hosting
About
Contact

Our logo is attached, it can be used light or dark.
Our only color used is the warm grey Pantone 8003C hex #877A69

You will only need to design the homepage to win the competition, but the winning designer will be required to supply without extra charges:
1. Home page design
2. A second, standard page template design
3. An icon set in colors appropriate to the site that have icons to match the subjects in these pages:
https://tavrinex.com.au/products/
https://tavrinex.com.au/making-the-switch/
https://tavrinex.com.au/why-tavrinex/
We will create a single page version of the options on https://tavrinex.com.au/solutions/
4.Any images used

Please avoid stock photos that are too common - e.g. smiling woman with headset, try to make the design stand out with simple images and well-designed layout.

Target Market(s)

Mid-size business clients

Industry/Entity Type

It Company

Number of Pages Required

1 page

Requirements
Must have
• Quor logo
• Use Quor color

```html
<!DOCTYPE html>
<html lang="en">
<head>
<meta charset="utf-8">
<title>Quor — IT Support for Business</title>
<link href="https://fonts.googleapis.com/css2?family=Raleway:wght@300;400;600;700&family=Open+Sans:wght@400;600&display=swap" rel="stylesheet">
<style>
:root{
  --brand:#877A69;
  --brand-dark:#6e6354;
  --accent:#d4a86a;
  --ink:#3b3631;
  --muted:#8c8a86;
  --line:#e4e1dc;
  --paper:#ffffff;
  --band:#f2f1ef;
  --footer:#2b2825;
  --footer-ink:#a9a39a;
}
*{box-sizing:border-box;margin:0;padding:0}
html,body{width:1200px;height:3440px;overflow:hidden}
body{font-family:"Open Sans",Arial,sans-serif;color:var(--ink);background:var(--paper);font-size:14px;line-height:1.6}
h1,h2,h3,h4{font-family:"Raleway",Arial,sans-serif;font-weight:600}
.section{position:relative;width:1200px;overflow:hidden}

/* hero */
.hero{height:520px}
.hero-photo{position:absolute;inset:0;background:linear-gradient(180deg,#4a4038 0%,#5d5247 45%,#3a332d 100%)}
.hero-shade{position:absolute;inset:0;background:rgba(30,26,22,.45)}
.topbar{position:absolute;top:14px;left:48px;right:48px;display:flex;justify-content:space-between;align-items:center}
.logo{display:flex;align-items:center;gap:10px;color:#fff;font-family:"Raleway",sans-serif;font-weight:600;font-size:20px}
.logo-box{width:40px;height:40px;border:0;background:var(--brand)}
.top-right{display:flex;align-items:center;gap:18px;color:#fff;font-weight:600;font-size:17px}
.login{display:flex;align-items:center;gap:6px;border:1px solid rgba(255,255,255,.7);padding:3px 12px;font-size:12px;border-radius:2px}
.nav{position:absolute;top:98px;left:0;right:0;display:flex;justify-content:center;gap:34px;font-size:12px;color:#fff}
.nav a{color:#fff;text-decoration:none}
.nav a.active{color:var(--accent);border-bottom:2px solid var(--accent);padding-bottom:4px}
.hero-title{position:absolute;top:232px;left:0;right:0;text-align:center;color:#fff;font-weight:300;font-size:52px}
.hero-title span{color:var(--accent);font-weight:400}
.hero-sub{position:absolute;top:302px;left:0;right:0;text-align:center;color:#e9e3da;font-size:13px}
.hero-arrow{position:absolute;top:256px;color:#fff;font-size:11px;letter-spacing:1px;display:flex;align-items:center;gap:6px}
.hero-arrow.prev{left:48px}
.hero-arrow.next{right:48px;color:var(--accent)}
.hero-scroll{position:absolute;top:432px;left:584px}

/* intro */
.intro{height:290px;display:flex;gap:60px;padding:60px 140px 0}
.intro-col{flex:1}
.intro-col h3{font-size:18px;margin-bottom:12px}
.intro-col p{font-size:12px;color:var(--muted);margin-bottom:14px}
.btn-outline{display:inline-block;border:1px solid var(--brand);color:var(--brand);font-size:11px;padding:4px 14px}

/* services */
.services{height:690px;border-top:1px solid var(--line)}
.section-title{text-align:center;font-size:20px;padding-top:28px}
.service-grid{position:absolute;top:90px;left:120px;right:120px;display:grid;grid-template-columns:repeat(3,1fr);row-gap:70px}
.service{text-align:center;padding:0 30px}
.service-icon{width:110px;height:110px;border-radius:50%;border:1px solid var(--line);margin:0 auto 18px;display:flex;align-items:center;justify-content:center;background:#fff}
.service-icon.on{background:var(--brand);border-color:var(--brand)}
.service h4{font-size:15px;margin-bottom:10px}
.service p{font-size:12px;color:var(--muted)}

/* voip band */
.voip{height:570px;background:var(--band)}
.voip-left{position:absolute;top:80px;left:150px;width:420px}
.voip-left h3{font-size:18px;margin-bottom:10px}
.voip-left p{font-size:12px;color:var(--muted)}
.devices{position:absolute;top:200px;left:150px;width:420px;height:240px;border-radius:6px;background:linear-gradient(135deg,#2e2c2a,#5b6a7a 55%,#9fb2c2)}
.feature-list{position:absolute;top:74px;left:610px;width:440px}
.feature{display:flex;gap:22px;margin-bottom:46px}
.feature h4{font-size:16px;margin-bottom:8px}
.feature p{font-size:12px;color:var(--muted)}

/* products */
.products{height:550px}
.products .section-title{padding-top:100px}
.product-row{position:absolute;top:170px;left:150px;right:150px;display:flex;gap:40px}
.product{flex:1;text-align:center;padding:16px 16px 20px;border:1px solid transparent}
.product.featured{border-color:var(--line);box-shadow:0 4px 16px rgba(0,0,0,.08)}
.product-img{height:130px;margin-bottom:16px;border-radius:3px}
.product h4{font-size:14px;margin-bottom:8px}
.product p{font-size:12px;color:var(--muted);margin-bottom:16px}
.btn-fill{display:inline-block;background:var(--brand);color:#fff;font-size:11px;padding:5px 16px}
.prod-arrow{position:absolute;top:340px;font-size:11px;display:flex;align-items:center;gap:6px}
.prod-arrow.prev{left:74px}
.prod-arrow.next{right:74px;color:var(--brand)}

/* partners */
.partners{height:170px;background:var(--band)}
.partners .section-title{font-size:18px;padding-top:26px}
.partner-row{position:absolute;top:96px;left:170px;right:170px;display:flex;justify-content:space-between}
.badge{width:100px;height:32px;background:#c9c3ba;border-radius:3px}

/* map */
.map{height:320px}
.map-fill{position:absolute;inset:0;background:linear-gradient(135deg,#e6e4e1,#d9d6d1)}
.contact-bar{position:absolute;top:10px;left:240px;right:240px;height:70px;background:#fff;box-shadow:0 3px 12px rgba(0,0,0,.12);display:flex;justify-content:space-around;align-items:center;font-size:11px;color:var(--muted);text-align:center}
.contact-bar div{display:flex;flex-direction:column;align-items:center;gap:4px}

/* footer */
.footer{height:330px;background:var(--footer);color:var(--footer-ink)}
.footer-cols{position:absolute;top:48px;left:150px;right:150px;display:grid;grid-template-columns:repeat(4,1fr)}
.footer-col{position:relative}
.footer-num{position:absolute;top:-36px;left:-6px;font-family:"Raleway",sans-serif;font-weight:700;font-size:72px;color:rgba(255,255,255,.05);line-height:1}
.footer-col h4{position:relative;color:#fff;font-size:15px;margin-bottom:14px}
.footer-col ul{list-style:none;font-size:11px;line-height:1.75}
.footer-col li.current{color:var(--accent)}
.footer-contact li{display:flex;gap:6px;align-items:center}
.copyright{position:absolute;bottom:12px;left:0;right:0;text-align:center;font-size:10px;border-top:1px solid rgba(255,255,255,.08);padding-top:10px}
</style>
</head>
<body>

<header class="section hero">
  <div class="hero-photo" role="img" aria-label="Photo of a business team in a meeting around a table"></div>
  <div class="hero-shade"></div>
  <div class="topbar">
    <div class="logo"><span class="logo-box"></span>Quor</div>
    <div class="top-right">
      <span>Phone: 0294713365</span>
      <span class="login">
        <svg width="10" height="12" viewBox="0 0 10 12"><rect x="1" y="5" width="8" height="6" fill="#fff"/><path d="M3 5V3.5a2 2 0 0 1 4 0V5" fill="none" stroke="#fff" stroke-width="1.3"/></svg>
        Log in
      </span>
    </div>
  </div>
  <nav class="nav">
    <a class="active" href="#">Home</a><a href="#">About</a><a href="#">VoIP</a><a href="#">IT Support</a><a href="#">Internet and Data</a><a href="#">Cloud Hosting</a><a href="#">Contact</a>
  </nav>
  <h1 class="hero-title"><span>IT Support</span> for Business</h1>
  <p class="hero-sub">We support the latest technology in place so your staff can focus on delivering your day-to-day business.</p>
  <div class="hero-arrow prev"><svg width="16" height="8"><path d="M16 4H2M5 1 2 4l3 3" fill="none" stroke="#fff"/></svg>PREV</div>
  <div class="hero-arrow next">NEXT<svg width="16" height="8"><path d="M0 4h14M11 1l3 3-3 3" fill="none" stroke="#d4a86a"/></svg></div>
  <svg class="hero-scroll" width="32" height="44" viewBox="0 0 32 44"><rect x="6" y="2" width="20" height="38" rx="4" fill="none" stroke="#fff" stroke-width="2"/><line x1="16" y1="10" x2="16" y2="18" stroke="#fff" stroke-width="2"/></svg>
</header>

<section class="section intro">
  <div class="intro-col">
    <h3>About Quor</h3>
    <p>Servicing Sydney's IT needs with experience in business technologies and platforms, with a focus on customer service. We pride ourselves on our skills, integrity and ability to think outside the box.</p>
    <span class="btn-outline">Explore More</span>
  </div>
  <div class="intro-col">
    <h3>Certified Technicians</h3>
    <p>Be confident that the skills required are available and certified — we have a broad range of expertise and continuously update our skills and certifications to keep pace.</p>
    <span class="btn-outline">Know More</span>
  </div>
</section>

<section class="section services">
  <h2 class="section-title">Services We Provide</h2>
  <div class="service-grid">
    <div class="service">
      <div class="service-icon"><svg width="40" height="28" viewBox="0 0 40 28"><path d="M10 26h22a7 7 0 0 0 0-14 10 10 0 0 0-19-3A8 8 0 0 0 10 26z" fill="none" stroke="#877A69" stroke-width="2"/></svg></div>
      <h4>Cloud Services</h4>
      <p>Quor provides a range of cloud services including hosted servers, backup and infrastructure as a service.</p>
    </div>
    <div class="service">
      <div class="service-icon on"><svg width="40" height="40" viewBox="0 0 40 40"><circle cx="20" cy="20" r="14" fill="none" stroke="#fff" stroke-width="2"/><circle cx="20" cy="20" r="6" fill="none" stroke="#fff" stroke-width="2"/><path d="M20 6v8M20 26v8M6 20h8M26 20h8" stroke="#fff" stroke-width="2"/></svg></div>
      <h4>Support</h4>
      <p>Regularly scheduled service visits and fast, friendly help so your technology is always up to standard.</p>
    </div>
    <div class="service">
      <div class="service-icon"><svg width="38" height="38" viewBox="0 0 38 38"><circle cx="19" cy="19" r="16" fill="none" stroke="#877A69" stroke-width="2"/><ellipse cx="19" cy="19" rx="7" ry="16" fill="none" stroke="#877A69" stroke-width="2"/><path d="M3 19h32" stroke="#877A69" stroke-width="2"/></svg></div>
      <h4>Data and Voice</h4>
      <p>Quor supplies a wide range of business data connections which are reliable, scalable and fairly priced.</p>
    </div>
    <div class="service">
      <div class="service-icon"><svg width="40" height="34" viewBox="0 0 40 34"><rect x="2" y="2" width="36" height="24" fill="none" stroke="#877A69" stroke-width="2"/><path d="M14 32h12M20 26v6" stroke="#877A69" stroke-width="2"/></svg></div>
      <h4>Web Design</h4>
      <p>So you can put your best foot forward, our designers build clean sites that are simple to manage.</p>
    </div>
    <div class="service">
      <div class="service-icon"><svg width="42" height="30" viewBox="0 0 42 30"><rect x="7" y="2" width="28" height="20" fill="none" stroke="#877A69" stroke-width="2"/><path d="M2 27h38" stroke="#877A69" stroke-width="2"/></svg></div>
      <h4>Software Integration</h4>
      <p>Check and integrate your programs, whether easy or complex, so your systems work together as one.</p>
    </div>
    <div class="service">
      <div class="service-icon"><svg width="38" height="36" viewBox="0 0 38 36"><path d="M19 2l5 11 12 1-9 8 3 12-11-6-11 6 3-12-9-8 12-1z" fill="none" stroke="#877A69" stroke-width="2"/></svg></div>
      <h4>IT Gurus</h4>
      <p>In-depth knowledge of HTML, CSS, servers, networks and the platforms your business relies on.</p>
    </div>
  </div>
</section>

<section class="section voip">
  <div class="voip-left">
    <h3>VoIP Services for Business</h3>
    <p>Quor supplies a wide range of business voice connections which are reliable, scalable and backed by excellent value-for-money plans.</p>
  </div>
  <div class="devices" role="img" aria-label="Desktop monitor, laptop, tablet and phone showing a dashboard"></div>
  <div class="feature-list">
    <div class="feature">
      <svg width="34" height="34" viewBox="0 0 34 34"><circle cx="17" cy="17" r="15" fill="none" stroke="#d4a86a" stroke-width="2"/><path d="M10 17l5 5 9-10" fill="none" stroke="#d4a86a" stroke-width="2.4"/></svg>
      <div><h4>VoIP For Business Support</h4><p>Quor partners with a wide range of suppliers providing voice, phone and data services so we can provide an integrated voice solution.</p></div>
    </div>
    <div class="feature">
      <svg width="34" height="34" viewBox="0 0 34 34"><circle cx="17" cy="17" r="15" fill="none" stroke="#d4a86a" stroke-width="2"/><path d="M10 17l5 5 9-10" fill="none" stroke="#d4a86a" stroke-width="2.4"/></svg>
      <div><h4>Hardware Integration</h4><p>We supply, configure and install hardware to work with your network, and understand the technical complexities of sharing it.</p></div>
    </div>
    <div class="feature">
      <svg width="34" height="34" viewBox="0 0 34 34"><circle cx="17" cy="17" r="15" fill="none" stroke="#d4a86a" stroke-width="2"/><path d="M10 17l5 5 9-10" fill="none" stroke="#d4a86a" stroke-width="2.4"/></svg>
      <div><h4>Hosted PBX</h4><p>For cost-effective, tailored phone systems in the cloud, we set up call routing and features so your team connects well.</p></div>
    </div>
  </div>
</section>

<section class="section products">
  <h2 class="section-title">Our Products</h2>
  <div class="prod-arrow prev"><svg width="16" height="8"><path d="M16 4H2M5 1 2 4l3 3" fill="none" stroke="#3b3631"/></svg>PREV</div>
  <div class="prod-arrow next">NEXT<svg width="16" height="8"><path d="M0 4h14M11 1l3 3-3 3" fill="none" stroke="#877A69"/></svg></div>
  <div class="product-row">
    <div class="product">
      <div class="product-img" role="img" aria-label="Desktop computer, laptop, tablet and phone" style="background:linear-gradient(135deg,#e9e7e4,#b9b4ad)"></div>
      <h4>Lumen Desk, Lumen Book, Lumen Pad and Lumen Phone</h4>
      <p>Great for home and the office. Sleek models and supplies you can easily integrate with your business.</p>
      <span class="btn-fill">Read More</span>
    </div>
    <div class="product featured">
      <div class="product-img" role="img" aria-label="Rack of standalone and blade servers" style="background:linear-gradient(135deg,#3c3a38,#7d7a76)"></div>
      <h4>Harlow Standalone and Blade Servers</h4>
      <p>The only server chassis to deliver multiple distributed and adaptable systems in one platform.</p>
      <span class="btn-fill">Read More</span>
    </div>
    <div class="product">
      <div class="product-img" role="img" aria-label="Office printers and copiers" style="background:linear-gradient(135deg,#f1f0ee,#c3beb7)"></div>
      <h4>Harlow Products and Vantor Printers</h4>
      <p>Your right-hand office partner. We'll look around at computer and printer needs, and we'll find the right fit.</p>
      <span class="btn-fill">Read More</span>
    </div>
  </div>
</section>

<section class="section partners">
  <h2 class="section-title">Some of Our Partners</h2>
  <div class="partner-row">
    <span class="badge"></span><span class="badge"></span><span class="badge"></span><span class="badge"></span><span class="badge"></span><span class="badge"></span>
  </div>
</section>

<section class="section map">
  <div class="map-fill" role="img" aria-label="Street map showing the office location"></div>
  <div class="contact-bar">
    <div><svg width="20" height="14" viewBox="0 0 20 14"><rect x="1" y="1" width="18" height="12" fill="none" stroke="#877A69" stroke-width="1.6"/><path d="M1 1l9 7 9-7" fill="none" stroke="#877A69" stroke-width="1.6"/></svg>info@quorvel.net</div>
    <div><svg width="14" height="18" viewBox="0 0 14 18"><path d="M7 17S1 10 1 6.5a6 6 0 0 1 12 0C13 10 7 17 7 17z" fill="none" stroke="#877A69" stroke-width="1.6"/><circle cx="7" cy="6.5" r="2" fill="#877A69"/></svg>Suite 6, 18 Kelham St, Redfern<br>NSW 2016</div>
    <div><svg width="16" height="16" viewBox="0 0 16 16"><path d="M3 1l3 3-2 2a9 9 0 0 0 6 6l2-2 3 3-2 2C7 15 1 9 1 3z" fill="none" stroke="#877A69" stroke-width="1.6"/></svg>0294713365</div>
  </div>
</section>

<footer class="section footer">
  <div class="footer-cols">
    <div class="footer-col">
      <span class="footer-num">01</span>
      <h4>Quick Links</h4>
      <ul><li class="current">Home</li><li>About</li><li>VoIP</li><li>IT Support</li><li>Internet and Data</li><li>Cloud Hosting</li><li>Contact</li></ul>
    </div>
    <div class="footer-col">
      <span class="footer-num">02</span>
      <h4>Our Services</h4>
      <ul><li>Cloud Services</li><li>Support</li><li class="current">Data and Voice</li><li>Web Design</li><li>Software Integration</li><li>IT Gurus</li></ul>
    </div>
    <div class="footer-col">
      <span class="footer-num">03</span>
      <h4>Our Support</h4>
      <ul><li>Online Support</li><li>Cloud Storage</li><li>Malware</li><li>Cryptolocker</li><li>Network</li><li>Service Contracts</li></ul>
    </div>
    <div class="footer-col footer-contact">
      <span class="footer-num">04</span>
      <h4>Contact Us</h4>
      <ul>
        <li>Suite 6, 18 Kelham St, Redfern NSW 2016</li>
        <li>Phone: +61 (2) 94713365</li>
        <li>Fax: +61 (2) 94713366</li>
        <li>Email: info@quorvel.net</li>
      </ul>
    </div>
  </div>
  <p class="copyright">Copyright 2017 Quor. All rights reserved.</p>
</footer>

</body>
</html>
```